IT Company needs a new Flyer Design

We are an expanding IT company based in Perth, Western Australia. When we first opened we produced a small flyer internally and letter box dropped to 100 business in our area (we are located in a newly developed and ever increasing commercial district). We had a good hit ratio and picked up a handful of local companies.
5 years has passed and we have grown significantly, we now feel the time is right to get out there are start canvasing the hundreds of new business which have opened in past couple of years in our area. We are the largest company of our type in the area by far with 10 staff (any other IT support companies in the area are 1 or 2 man bands).
Our Key strength is our Complete IT Management approach, giving our clients a complete rang of services from traditional IT Services (Support, Servers, Workstations, Printers), Electrical (Data Cabling, All Electrical Work, Exit Light Testing, Testing and Tagging), Web Division (SEO, Websites, Copy Writing etc), Offsite Backup and Cloud Solutions, Phone systems and Security systems integrating CCTV and Access Control.
I have attached the first flyer we produced internally, as well as Company Logo's etc. Feel free to re-write the text, the text still gets the message across, but happy for it to have some create flare added.
The aim of this brochure is to introduce ourselves and also the fact that we are in the local area.
The target market will be business owners.
Business

```html
<!DOCTYPE html>
<html lang="en">
<head>
<meta charset="utf-8">
<title>Harbour Networks – Flyer</title>
<link rel="stylesheet" href="https://fonts.googleapis.com/css2?family=Open+Sans:wght@300;400;600;700;800&display=swap">
<style>
  :root{
    --page:#ffffff;
    --panel:#e4e4e4;
    --heading:#55687a;
    --body:#7b8894;
    --list:#5f6f7e;
    --accent:#1a9ad6;
    --rule:#aab3ba;
    --logo:#5e6c78;
  }
  *{box-sizing:border-box;margin:0;padding:0}
  html,body{width:1200px;height:1000px;overflow:hidden;background:var(--page)}
  body{position:relative;font-family:"Open Sans",Arial,sans-serif}
  .panel{position:absolute;left:18px;top:90px;width:1162px;height:810px;background:var(--panel)}
  .url{position:absolute;top:106px;font-size:12px;color:var(--body);font-weight:400}
  .url--left{left:38px}
  .url--right{right:40px}
  .rule{position:absolute;height:1px;background:var(--rule)}
  .rule--top{left:205px;width:785px;top:115px}
  .rule--bottom{left:205px;width:785px;top:879px}
  .heading{position:absolute;top:152px;width:300px;text-align:center;font-size:25px;font-weight:800;color:var(--heading);letter-spacing:.3px;text-shadow:1px 1px 1px rgba(255,255,255,.9),2px 2px 2px rgba(0,0,0,.18)}
  .heading--what{left:70px}
  .heading--install{left:450px}
  .heading--support{left:829px}
  .icon{position:absolute}
  .icon--plane{left:178px;top:208px}
  .icon--arrows{left:556px;top:208px}
  .icon--phone{left:938px;top:212px}
  .copy{position:absolute;top:341px;font-size:16px;font-weight:300;line-height:25.8px;color:var(--body)}
  .copy p{margin-bottom:25.8px}
  .copy--what{left:37px;width:350px}
  .copy--support{left:802px;width:362px}
  .services{position:absolute;left:476px;top:341px;width:300px}
  .services ul{list-style:none}
  .services li{position:relative;padding-left:25px;font-size:16px;font-weight:600;line-height:25.7px;color:var(--list)}
  .services li::before{content:"";position:absolute;left:2px;top:8px;width:12px;height:10px;background:
    linear-gradient(var(--list),var(--list));
    clip-path:polygon(0 0,45% 50%,0 100%,15% 100%,60% 50%,15% 0,45% 0,90% 50%,45% 100%,60% 100%,100% 50%,60% 0)}
  .services .divider{height:1px;background:var(--rule);margin:12px 0 13px -46px;width:342px}
  .brand{position:absolute;top:842px;display:flex;align-items:center;gap:8px}
  .brand--left{left:37px}
  .brand--right{left:1032px}
  .brand__mark{width:28px;height:28px;background:var(--logo)}
  .brand__name{font-size:14px;font-weight:800;line-height:15px;color:var(--logo);width:96px}
</style>
</head>
<body>
  <div class="panel"></div>

  <span class="url url--left">www.harbournetworks.com.au</span>
  <span class="url url--right">www.harbournetworks.com.au</span>
  <div class="rule rule--top"></div>

  <h2 class="heading heading--what">WHAT WE DO</h2>
  <h2 class="heading heading--install">INSTALLATION</h2>
  <h2 class="heading heading--support">SUPPORT</h2>

  <svg class="icon icon--plane" width="84" height="86" viewBox="0 0 84 86" aria-hidden="true">
    <polygon points="2,2 82,38 30,40" fill="var(--accent)"/>
    <polygon points="2,2 30,40 14,70" fill="var(--accent)"/>
    <polygon points="42,60 56,46 57,84" fill="var(--accent)"/>
  </svg>

  <svg class="icon icon--arrows" width="86" height="86" viewBox="0 0 86 86" aria-hidden="true">
    <polygon points="2,9 9,2 27,20 33,14 33,36 11,36 17,30" fill="var(--accent)"/>
    <polygon points="84,77 77,84 59,66 53,72 53,50 75,50 69,56" fill="var(--accent)"/>
  </svg>

  <svg class="icon icon--phone" width="80" height="80" viewBox="0 0 24 24" aria-hidden="true">
    <path fill="var(--accent)" d="M6.62 10.79c1.44 2.83 3.76 5.14 6.59 6.59l2.2-2.2c.27-.27.67-.36 1.02-.24 1.12.37 2.33.57 3.57.57.55 0 1 .45 1 1V20c0 .55-.45 1-1 1-9.39 0-17-7.61-17-17 0-.55.45-1 1-1h3.5c.55 0 1 .45 1 1 0 1.25.2 2.45.57 3.57.11.35.03.74-.25 1.02l-2.2 2.2z"/>
  </svg>

  <div class="copy copy--what">
    <p>Harbour Networks specialises in providing complete IT management for small to medium size business.</p>
    <p>We provide installation and maintenance of complete managed networks with a focus on ongoing management.</p>
    <p>Harbour works in a clear, concise and professional manner to ensure that every area of your business IT requirements are effectively managed.</p>
    <p>Allowing you the freedom to run your business</p>
  </div>

  <div class="services">
    <ul>
      <li>Networking</li>
      <li>Servers</li>
      <li>Workstations</li>
      <li>Laptops</li>
      <li>Firewalls</li>
    </ul>
    <div class="divider"></div>
    <ul>
      <li>Data Cabling</li>
      <li>All electrical Work</li>
      <li>Server Racks</li>
      <li>Network Infrastructure</li>
      <li>Off site back up</li>
    </ul>
    <div class="divider"></div>
    <ul>
      <li>ADSL Connections</li>
      <li>Web Hosting</li>
      <li>Web Design</li>
      <li>Website Maintenance</li>
      <li>Domain Names PABX systems</li>
    </ul>
  </div>

  <div class="copy copy--support">
    <p>Unlike organisation who offer one level of service, Harbour Networks is equipped to offer a lage range of support agreements depending on your needs and budget.</p>
    <p>Whether you require ad-hoc support when things go wrong, or you’re after complete seamless management of all your communications and technology equipment, Harbour has qualified and experienced staff to take care of your needs.</p>
    <p>Harbour Networks understands that things always malfunction at the least convenient time, so we offer hours support to make sure small problems don’t turn into disasters.</p>
  </div>

  <div class="brand brand--left">
    <span class="brand__mark"></span>
    <span class="brand__name">HARBOUR NETWORKS</span>
  </div>
  <div class="brand brand--right">
    <span class="brand__mark"></span>
    <span class="brand__name">HARBOUR NETWORKS</span>
  </div>
  <div class="rule rule--bottom"></div>
</body>
</html>
```